Legal Stationary

A full set of stationery is required
The image and logo, along with colour, are set and attached.
The style should be modern, clean, and corporate. Not just a basic template off the web.
In addition to the address/website/email/phone fields for KP and LCB number, with the text “the firm is authorised and regulated by the LCB”
All files in all formats will be needed to allow editing after. Initial setup of templates will be required, and details for 4 business cards will be supplied.
Consumers of legal services
Legal

```html
<!DOCTYPE html>
<html lang="en">
<head>
<meta charset="utf-8">
<title>Halvern Law – Stationery Set</title>
<link rel="stylesheet" href="https://fonts.googleapis.com/css2?family=Montserrat:wght@400;500;600;700&display=swap">
<style>
  :root{
    --brand:#243b94;
    --brand-dark:#1d3080;
    --paper:#ffffff;
    --ground:#e1e2e5;
    --ink:#3b3b3b;
    --muted:#6d6d6d;
    --rule:#c9c9c9;
    --row:#f0f0f0;
  }
  *{box-sizing:border-box;margin:0;padding:0}
  html,body{width:1039px;height:1200px;overflow:hidden}
  body{background:var(--ground);font-family:'Montserrat',sans-serif;color:var(--ink);position:relative}
  .piece{position:absolute;background:var(--paper);overflow:hidden}
  .piece.blue{background:var(--brand)}

  /* wordmark */
  .logo{display:inline-flex;align-items:center;gap:.35em;font-weight:600;letter-spacing:.04em;color:var(--brand);white-space:nowrap;line-height:1}
  .logo .logo-square{width:.7em;height:.7em;background:currentColor;display:inline-block}
  .blue .logo,.logo.on-blue{color:#fff}
  .center{position:absolute;left:0;right:0;display:flex;justify-content:center}

  .tagline{position:absolute;left:0;right:0;text-align:center;color:#fff}
  .icon{display:inline-block;vertical-align:middle;margin-right:3px}

  /* business card front */
  .card-front{left:52px;top:81px;width:283px;height:161px;border-radius:7px}
  .card-front .holder{position:absolute;right:151px;top:102px;text-align:right}
  .holder-name{font-weight:600;color:var(--brand);font-size:10px}
  .holder-role{font-size:8px;color:var(--ink)}
  .card-front .divider{position:absolute;left:141px;top:86px;width:1px;height:52px;background:#888}
  .card-front .contact{position:absolute;left:146px;top:85px;font-size:7.8px;line-height:10px;color:var(--ink)}

  .card-back{left:52px;top:251px;width:283px;height:161px;border-radius:7px}

  /* letterhead */
  .letterhead{left:353px;top:78px;width:237px;height:335px}
  .letter-body{position:absolute;left:24px;top:80px;width:188px;font-size:4.2px;line-height:5.6px;color:#555}
  .letter-body p{margin-bottom:5px;text-align:justify}
  .signature{width:24px;height:20px;background:linear-gradient(90deg,#e9e9e9,#f6f6f6);margin-top:4px}
  .letter-foot{position:absolute;left:24px;right:24px;top:296px;border-top:1px solid #999;padding-top:7px;text-align:center;font-size:5.5px;line-height:8px;color:var(--ink)}

  /* envelopes */
  .envelope-back{left:605px;top:81px;width:371px;height:173px}
  .envelope-back .return{position:absolute;left:30px;top:18px;text-align:center;font-size:6px;line-height:8px;color:var(--ink)}
  .envelope-front{left:605px;top:269px;width:371px;height:178px}
  .envelope-front svg{position:absolute;left:0;top:0}
  .envelope-front .tagline{color:var(--muted);top:148px;font-size:8.5px}

  /* invoice */
  .invoice{left:53px;top:423px;width:258px;height:360px}
  .invoice .head{position:absolute;left:17px;top:57px;width:224px;font-size:4.6px;color:var(--ink)}
  .invoice-title{font-weight:700;color:var(--brand);font-size:7.5px;display:flex;justify-content:space-between;align-items:baseline;margin-bottom:4px}
  .invoice-title small{font-size:4.6px;color:var(--ink);margin-right:36px}
  .field{display:flex;align-items:flex-end;gap:3px;height:10px}
  .field .line{flex:1;border-bottom:.6px solid #888;height:1px;margin-bottom:1px}
  .items{position:absolute;left:17px;top:105px;width:224px;border-collapse:collapse;font-size:5.4px}
  .items th{background:var(--brand);color:#fff;font-weight:600;height:14px}
  .items td{height:13px;border-left:.6px solid var(--brand);border-right:.6px solid var(--brand)}
  .items tr:nth-child(even) td{background:var(--row)}
  .items tr:last-child td{border-bottom:.6px solid var(--brand)}
  .totals{position:absolute;left:164px;top:264px;width:77px;border-collapse:collapse;font-size:4.6px;font-weight:600}
  .totals td{border:.6px solid var(--brand);height:13px;padding-left:6px}
  .payment{position:absolute;left:17px;top:271px;width:142px;display:flex;gap:6px;font-size:4.6px;white-space:nowrap}
  .payment span::before{content:"";display:inline-block;width:5px;height:5px;border:.6px solid var(--brand);margin-right:2px;vertical-align:-1px}
  .terms{position:absolute;left:17px;top:292px;font-size:4.6px;line-height:6.5px}
  .invoice .foot{position:absolute;left:0;right:0;top:329px;text-align:center;font-size:6px;line-height:8px}

  /* compliment card */
  .slip{left:353px;top:425px;width:180px;height:68px}
  .slip .holder{position:absolute;left:16px;top:13px}
  .slip .holder-name{font-size:5.4px}
  .slip .holder-role{font-size:4px}
  .slip .logo{position:absolute;right:16px;top:13px;font-size:8px}
  .slip .contact{position:absolute;left:16px;top:39px;font-size:4px;line-height:5.5px}
  .slip .address{position:absolute;right:16px;top:45px;font-size:4px;line-height:5px;text-align:right}

  /* notebooks */
  .notebook{left:358px;top:508px;width:187px;height:265px;overflow:visible}
  .rings{position:absolute;left:-9px;top:12px;display:flex;flex-direction:column;gap:11px}
  .rings i{display:block;width:17px;height:7px;border:1.6px solid #1b1b1b;border-radius:4px}
  .notebook .cover-mark{position:absolute;left:14px;right:0;top:122px;display:flex;justify-content:center}
  .notebook .tagline{top:237px;left:14px;font-size:5px}
  .spread{left:597px;top:506px;width:360px;height:264px;background:transparent;overflow:visible}
  .page{position:absolute;top:0;width:180px;height:264px;background:var(--paper);padding:40px 12px 0;
    background-image:repeating-linear-gradient(to bottom,transparent 0 7px,#cfcfcf 7px 7.6px);background-origin:content-box;background-clip:content-box}
  .page.left{left:0}
  .page.right{left:180px}
  .page .logo{position:absolute;top:16px;font-size:9px}
  .page.left .logo{left:16px}
  .page.right .logo{left:24px;top:12px}
  .spread .rings{left:171px;top:10px;gap:11px}

  /* presentation folders */
  .folder-back{left:60px;top:880px;width:180px;height:240px}
  .folder-back .contact{position:absolute;left:20px;bottom:26px;font-size:5.5px;line-height:7.5px;color:#fff}
  .folder-front{left:240px;top:880px;width:180px;height:240px}
  .folder-front .tagline{color:var(--brand);top:205px;font-size:5.5px}
  .folder-inside{left:560px;top:880px;width:360px;height:240px;background:transparent;overflow:visible}
  .folder-inside .page{background:var(--paper);background-image:none;padding:0}
  .folder-inside svg{position:absolute;left:0;top:0}
  .pocket-card{position:absolute;left:270px;top:175px;width:80px;height:42px;background:#fff;border-radius:3px;padding:5px}
  .pocket-card .logo{font-size:6px}
  .pocket-card .holder-name{font-size:3.6px;margin-top:6px}
  .pocket-card .holder-role{font-size:3px}
</style>
</head>
<body>

<!-- business card, front -->
<section class="piece card-front">
  <div class="center" style="top:27px"><span class="logo" style="font-size:26px"><span class="logo-square"></span>HALVERN LAW</span></div>
  <div class="holder">
    <div class="holder-name">CORIN MADDOX</div>
    <div class="holder-role">Managing Director</div>
  </div>
  <div class="divider"></div>
  <div class="contact">
    58 Alder Court<br>Brookfield, CA 90412<br>
    <span class="icon" style="width:6px;height:6px;border:1px solid var(--brand);border-radius:1px"></span>+39 300 5550147<br>
    <span class="icon" style="width:6px;height:6px;background:var(--brand);border-radius:1px"></span>office@halvernlaw.example<br>
    <span class="icon" style="width:6px;height:6px;background:var(--brand);border-radius:50%"></span>www.halvernlaw.example
  </div>
</section>

<!-- business card, back -->
<section class="piece blue card-back">
  <div class="center" style="top:64px"><span class="logo" style="font-size:26px"><span class="logo-square"></span>HALVERN LAW</span></div>
  <p class="tagline" style="top:136px;font-size:7px">The firm is authorised and regulated by the LCB</p>
</section>

<!-- letterhead -->
<section class="piece letterhead">
  <div class="center" style="top:21px"><span class="logo" style="font-size:13px"><span class="logo-square"></span>HALVERN LAW</span></div>
  <div class="letter-body">
    <p>Dear customer,</p>
    <p>Thank you for choosing our firm. This letter confirms the scope of our work, the fees agreed and the people who will handle your matter day to day.</p>
    <p>Please read the enclosed terms with care and keep them for your records. If anything is unclear, contact your adviser and we will gladly explain it in plain language.</p>
    <p>We will keep you informed at each stage, reply to messages within two working days and send a written update whenever a key deadline or decision is close.</p>
    <p>Our fees are billed monthly and may be settled by card or bank transfer.</p>
    <p>Yours Sincerely,</p>
    <p style="margin-top:10px;margin-bottom:0">Elias Ward<br>General Director</p>
    <div class="signature" role="img" aria-label="Handwritten signature"></div>
  </div>
  <div class="letter-foot">
    58 Alder Court Brookfield, CA 90412<br>
    555.014.2286 &nbsp; office@halvernlaw.example &nbsp; www.halvernlaw.example
  </div>
</section>

<!-- envelope, back -->
<section class="piece envelope-back">
  <div class="return">
    <span class="logo" style="font-size:13px;margin-bottom:4px"><span class="logo-square"></span>HALVERN LAW</span><br>
    710 Harbor Lane, Suite 4<br>Easton, MA 02101 USA
  </div>
</section>

<!-- envelope, front with flap -->
<section class="piece envelope-front">
  <svg width="371" height="178" viewBox="0 0 371 178" aria-hidden="true">
    <path d="M0 0H371L355 30Q348 40 334 42L185 65L37 42Q23 40 16 30Z" fill="var(--brand)"/>
  </svg>
  <div class="center" style="top:20px"><span class="logo on-blue" style="font-size:15px"><span class="logo-square"></span>HALVERN LAW</span></div>
  <p class="tagline">The firm is authorised and regulated by the LCB</p>
</section>

<!-- invoice -->
<section class="piece invoice">
  <div class="center" style="top:24px"><span class="logo" style="font-size:15px"><span class="logo-square"></span>HALVERN LAW</span></div>
  <div class="head">
    <div class="invoice-title">INVOICE # : <small>DATE :</small></div>
    <div class="field">Customer :<span class="line"></span></div>
    <div class="field">Address :<span class="line"></span></div>
    <div class="field">Phone :<span class="line" style="flex:.9"></span>Fax :<span class="line"></span></div>
  </div>
  <table class="items">
    <thead><tr><th style="width:30px">QTY</th><th style="width:117px">DESCRIPTION</th><th style="width:38px">PRICE</th><th style="width:39px">AMOUNT</th></tr></thead>
    <tbody>
      <tr><td></td><td></td><td></td><td></td></tr><tr><td></td><td></td><td></td><td></td></tr>
      <tr><td></td><td></td><td></td><td></td></tr><tr><td></td><td></td><td></td><td></td></tr>
      <tr><td></td><td></td><td></td><td></td></tr><tr><td></td><td></td><td></td><td></td></tr>
      <tr><td></td><td></td><td></td><td></td></tr><tr><td></td><td></td><td></td><td></td></tr>
      <tr><td></td><td></td><td></td><td></td></tr><tr><td></td><td></td><td></td><td></td></tr>
      <tr><td></td><td></td><td></td><td></td></tr>
    </tbody>
  </table>
  <div class="payment"><span>CARD</span><span>BANK</span><span>DEBIT</span><span>CASH</span><span>CHEQUE</span></div>
  <table class="totals">
    <tr><td style="width:39px">SUB TOTAL</td><td></td></tr>
    <tr><td>GST #</td><td></td></tr>
    <tr><td>SUBTOTAL</td><td></td></tr>
  </table>
  <p class="terms">Signature Indicates<br>Acceptance of Price and term</p>
  <p class="foot">58 Alder Court Brookfield, CA 90412<br>555.014.2286 &nbsp; office@halvernlaw.example &nbsp; www.halvernlaw.example</p>
</section>

<!-- compliment slip card -->
<section class="piece slip">
  <div class="holder">
    <div class="holder-name">CORIN MADDOX</div>
    <div class="holder-role">Managing Director</div>
  </div>
  <span class="logo"><span class="logo-square"></span>HALVERN LAW</span>
  <div class="contact">+39 300 5550147<br>office@halvernlaw.example<br>www.halvernlaw.example</div>
  <div class="address">58 Alder Court<br>Brookfield, CA 90412</div>
</section>

<!-- notebook cover -->
<section class="piece blue notebook">
  <div class="rings"><i></i><i></i><i></i><i></i><i></i><i></i><i></i><i></i><i></i><i></i><i></i><i></i><i></i><i></i></div>
  <div class="cover-mark"><span class="logo" style="font-size:14px"><span class="logo-square"></span>HALVERN LAW</span></div>
  <p class="tagline">The firm is authorised and regulated by the LCB</p>
</section>

<!-- notebook, open -->
<section class="piece spread">
  <div class="page left"><span class="logo"><span class="logo-square"></span>HALVERN LAW</span></div>
  <div class="page right"><span class="logo"><span class="logo-square"></span>HALVERN LAW</span></div>
  <div class="rings"><i></i><i></i><i></i><i></i><i></i><i></i><i></i><i></i><i></i><i></i><i></i><i></i><i></i><i></i></div>
</section>

<!-- presentation folder, outside -->
<section class="piece blue folder-back">
  <div class="contact">
    +39 300 5550147 | office@halvernlaw.example<br>
    58 Alder Court Brookfield, CA 90412<br>
    www.halvernlaw.example
  </div>
</section>
<section class="piece folder-front">
  <div class="center" style="top:100px"><span class="logo" style="font-size:16px"><span class="logo-square"></span>HALVERN LAW</span></div>
  <p class="tagline">The firm is authorised and regulated by the LCB</p>
</section>

<!-- presentation folder, inside -->
<section class="piece folder-inside">
  <div class="page left"></div>
  <div class="page right"></div>
  <svg width="360" height="240" viewBox="0 0 360 240" aria-hidden="true">
    <path d="M0 160L172 146L180 240H0Z" fill="var(--brand)"/>
    <path d="M186 148L360 125V240H186Z" fill="var(--brand)"/>
  </svg>
  <div class="pocket-card">
    <span class="logo"><span class="logo-square"></span>HALVERN LAW</span>
    <div class="holder-name">CORIN MADDOX</div>
    <div class="holder-role">Managing Director</div>
  </div>
</section>

</body>
</html>
```